residential roofing company needs a Truck wrap design.

We need a Van wrap design. We are a local residential roofing contractor.That specialize in Roofing Eavestrough and siding we need a design that will stand out and look professional.We really want roofing to stand out as that's our main focus. We like a clean a simple and modern design. Our website is www.larkfieldexteriors.ca The van we are wrapping is a 2019 Halvorsen-Kraft Tolvane 2500 Cargo 170 WB High Roof. We want to incorporate our phone number 844 612 DECK

```html
<!DOCTYPE html>
<html lang="en">
<head>
<meta charset="utf-8">
<title>Larkfield Exteriors – Van Wrap</title>
<link rel="stylesheet" href="https://fonts.googleapis.com/css2?family=Lato:wght@700;900&family=Roboto+Condensed:wght@500&family=Arimo&display=swap">
<style>
  :root {
    --wrap-yellow: #fdb607;
    --wrap-white: #ffffff;
    --brand-grey: #616163;
    --ink: #111111;
    --glass: #55575a;
    --page: #ffffff;
  }
  html, body {
    margin: 0;
    padding: 0;
    width: 1200px;
    height: 1076px;
    overflow: hidden;
    background: var(--page);
  }
  .wrap-sheet { display: block; width: 1200px; height: 1076px; }
  .van-body-base { fill: var(--wrap-white); stroke: #d9d9d9; stroke-width: 2; }
  .wrap-yellow { fill: var(--wrap-yellow); }
  .cab-window { fill: var(--glass); }
  .brand-mark { fill: var(--wrap-yellow); }
  .brand-name { font-family: "Lato", sans-serif; font-weight: 900; fill: var(--brand-grey); }
  .slogan { font-family: "Lato", sans-serif; font-weight: 700; fill: var(--ink); font-size: 44px; }
  .services-band { fill: var(--wrap-yellow); }
  .services { font-family: "Lato", sans-serif; font-weight: 700; fill: var(--ink); font-size: 38px; }
  .phone { font-family: "Roboto Condensed", sans-serif; font-weight: 500; fill: var(--wrap-yellow); font-size: 54px; }
  .phone-icon { fill: var(--wrap-yellow); }
  .website { font-family: "Arimo", sans-serif; fill: var(--ink); font-size: 34px; }
</style>
</head>
<body>
<svg class="wrap-sheet" viewBox="0 0 2030 1815" preserveAspectRatio="none" xmlns="http://www.w3.org/2000/svg">
  <defs>
    <path id="van-body" d="M55,700 L60,520 Q110,470 300,440 L475,240 Q560,150 700,100 L1890,80 Q1935,90 1948,150 L1980,600 L1982,718 L1655,728 Q1640,590 1530,588 Q1420,590 1408,735 L432,742 Q425,600 300,595 Q180,600 175,720 Z"/>
    <clipPath id="van-clip"><use href="#van-body"/></clipPath>
    <path id="phone-glyph" d="M6,2 Q0,4 1,12 Q4,28 18,36 Q24,39 28,34 L30,30 Q31,27 28,25 L22,21 Q19,20 17,22 L15,24 Q9,20 7,13 L9,11 Q11,9 10,6 L8,1 Q7,0 6,2 Z"/>
  </defs>

  <!-- Option A: roof-peak layout -->
  <g class="van-side van-side--peak">
    <use href="#van-body" class="van-body-base"/>
    <g clip-path="url(#van-clip)">
      <polygon class="wrap-yellow" points="0,0 950,0 950,95 485,565 0,565"/>
      <polygon class="wrap-yellow" points="1025,92 1122,88 520,563"/>
      <polygon class="wrap-yellow" points="1128,88 1200,88 1715,565 1690,565"/>
      <polygon class="wrap-yellow" points="1280,85 2030,70 2030,565 1755,565"/>
      <rect class="wrap-yellow" x="0" y="668" width="2030" height="120"/>
    </g>
    <path class="cab-window" d="M325,460 L490,265 Q505,250 530,248 L650,235 Q665,236 662,255 L640,395 Q635,410 615,413 L330,462 Z"/>

    <rect class="brand-mark" x="1060" y="155" width="130" height="130"/>
    <text class="brand-name" x="1124" y="372" text-anchor="middle" font-size="58">LARKFIELD</text>
    <text class="brand-name" x="1124" y="425" text-anchor="middle" font-size="46">EXTERIORS</text>

    <text class="slogan" x="1122" y="494" text-anchor="middle">ROOFING DONE RIGHT</text>
    <rect class="services-band" x="680" y="510" width="900" height="40"/>
    <text class="services" x="1128" y="540" text-anchor="middle">Roofing | Siding | Windows &amp; Doors | Eavestroughs</text>
    <use href="#phone-glyph" class="phone-icon" x="910" y="562"/>
    <text class="phone" x="1125" y="600" text-anchor="middle">844 612 DECK</text>
    <text class="website" x="1124" y="641" text-anchor="middle">www.larkfieldexteriors.ca</text>
  </g>

  <!-- Option B: sweep layout -->
  <g class="van-side van-side--sweep" transform="translate(0,910)">
    <use href="#van-body" class="van-body-base"/>
    <g clip-path="url(#van-clip)">
      <polygon class="wrap-yellow" points="0,0 835,0 835,95 445,565 0,565"/>
      <polygon class="wrap-yellow" points="900,95 980,95 475,565"/>
      <polygon class="wrap-yellow" points="1820,130 1470,565 1420,565"/>
      <polygon class="wrap-yellow" points="1900,75 2030,75 2030,565 1515,565"/>
      <rect class="wrap-yellow" x="0" y="668" width="2030" height="120"/>
    </g>
    <path class="cab-window" d="M325,460 L490,265 Q505,250 530,248 L650,235 Q665,236 662,255 L640,395 Q635,410 615,413 L330,462 Z"/>

    <rect class="brand-mark" x="868" y="208" width="145" height="145"/>
    <text class="brand-name" x="1048" y="285" font-size="60">LARKFIELD</text>
    <text class="brand-name" x="1048" y="335" font-size="48">EXTERIORS</text>

    <text class="slogan" x="1110" y="428" text-anchor="middle">ROOFING DONE RIGHT</text>
    <rect class="services-band" x="665" y="455" width="900" height="40"/>
    <text class="services" x="1112" y="484" text-anchor="middle">Roofing | Siding | Windows &amp; Doors | Eavestroughs</text>
    <use href="#phone-glyph" class="phone-icon" x="920" y="520"/>
    <text class="phone" x="1135" y="560" text-anchor="middle">844 612 DECK</text>
    <text class="website" x="1112" y="607" text-anchor="middle">www.larkfieldexteriors.ca</text>
  </g>
</svg>
</body>
</html>
```